Business card for Eyelash extension salon in Beverly Hills,California USA

We need new business card for our salon in Beverly Hills. The salon name is 'Lumarra' . We would like to have...Business name: Lumarra Name of person: will provide later Address 6128 N.Corbel Ridge Blvd Corvale Heights , CA 90377 Phone: will provide later (Text only) Web: www.lumarrastudio-example.com Pictogrid icon, Friendvale icon follow us for seasonal campaign and news @lumarrastudioexample Design should look elegant, high-end, clean, simple, cohesive with my brand. Please refer my brand board. Business name color will be metallic bronzy color. Im thinking grey background or white background. Thanks

Target Market(s)

25-35. Gender neutral. People who are in Entertainment business industry.
This is High-end Eyelash extension salon in Beverly Hills

Industry/Entity Type

Beauty Salon

Contact Information for Business Card

Business name: Lumarra
Name of person: will provide later
Address 6128 N.Corbel Ridge Blvd Corvale Heights , CA 90377
Phone: will provide later (Text only)
Web: www.lumarrastudio-example.com
Pictogrid icon, Friendvale icon
follow us for seasonal campaign and news @lumarrastudioexample

Requirements
Must have
• Beautiful, elegant, clean and simple look but very attractive and modern
Should not have
• We don't like too clutter, too busy designs.

```html
<!DOCTYPE html>
<html lang="en">
<head>
<meta charset="utf-8">
<title>Lumarra Business Card</title>
<link href="https://fonts.googleapis.com/css2?family=Cormorant+Garamond:wght@500;600&family=DM+Serif+Display&display=swap" rel="stylesheet">
<style>
  :root {
    --backdrop: #1f1f1f;
    --card-bronze: #8a6b54;
    --card-bronze-light: #927560;
    --ink-white: #ffffff;
    --logo-silver: #e6e1dc;
  }
  html, body {
    margin: 0;
    padding: 0;
    width: 1200px;
    height: 900px;
    overflow: hidden;
    background: var(--backdrop);
  }
  .canvas {
    position: relative;
    width: 1200px;
    height: 900px;
    display: flex;
    flex-direction: column;
    align-items: center;
    justify-content: center;
    gap: 40px;
  }
  .card {
    position: relative;
    width: 630px;
    height: 360px;
    background: var(--card-bronze);
    box-sizing: border-box;
  }
  .card--front {
    background: linear-gradient(135deg, var(--card-bronze) 0%, var(--card-bronze-light) 100%);
    display: flex;
    align-items: center;
    justify-content: center;
  }
  .brand-name {
    font-family: "Cormorant Garamond", Georgia, serif;
    font-weight: 500;
    font-size: 84px;
    letter-spacing: 2px;
    color: var(--logo-silver);
    margin: 0;
  }
  .card--back {
    color: var(--ink-white);
    font-family: "Cormorant Garamond", Georgia, serif;
    font-weight: 500;
    font-variant-numeric: lining-nums;
  }
  .identity {
    position: absolute;
    left: 50px;
    top: 132px;
    width: 250px;
    text-align: right;
  }
  .identity__name {
    font-family: "DM Serif Display", Georgia, serif;
    font-size: 28px;
    margin: 0;
    line-height: 1.1;
    white-space: nowrap;
  }
  .identity__role {
    font-size: 18px;
    margin: 2px 0 0;
  }
  .divider {
    position: absolute;
    left: 322px;
    top: 140px;
    width: 1px;
    height: 66px;
    background: var(--ink-white);
  }
  .contact-list {
    position: absolute;
    left: 342px;
    top: 138px;
    margin: 0;
    padding: 0;
    list-style: none;
    font-size: 17px;
    line-height: 23px;
    white-space: nowrap;
  }
  .contact-list li {
    display: flex;
    align-items: center;
    gap: 9px;
  }
  .contact-list svg {
    width: 11px;
    height: 11px;
    flex: none;
  }
  .contact-list .web {
    font-weight: 600;
    letter-spacing: 0.2px;
  }
  .address {
    position: absolute;
    left: 80px;
    bottom: 48px;
    font-size: 19px;
    margin: 0;
    white-space: nowrap;
  }
</style>
</head>
<body>
<main class="canvas">
  <section class="card card--front" aria-label="Card front">
    <h1 class="brand-name">Lumarra</h1>
  </section>

  <section class="card card--back" aria-label="Card back">
    <div class="identity">
      <p class="identity__name">Clara J. Whitfield</p>
      <p class="identity__role">Director</p>
    </div>
    <div class="divider"></div>
    <ul class="contact-list">
      <li>
        <svg viewBox="0 0 10 10" aria-hidden="true"><path d="M2 0.8 L3.6 0.8 L4.2 3 L3 3.8 Q4 6 6.2 7 L7 5.8 L9.2 6.4 L9.2 8 Q9.2 9.2 8 9.2 Q1 8.6 0.8 2 Q0.8 0.8 2 0.8 Z" fill="#fff"/></svg>
        <span>310.555.0148</span>
      </li>
      <li>
        <svg viewBox="0 0 10 10" aria-hidden="true"><rect x="0.7" y="2" width="8.6" height="6" fill="none" stroke="#fff" stroke-width="1"/><path d="M0.7 2 L5 5.4 L9.3 2" fill="none" stroke="#fff" stroke-width="1"/></svg>
        <span>hello.lumarra@example.com</span>
      </li>
      <li>
        <svg viewBox="0 0 10 10" aria-hidden="true"><circle cx="5" cy="5" r="4.3" fill="none" stroke="#fff" stroke-width="0.9"/><ellipse cx="5" cy="5" rx="1.9" ry="4.3" fill="none" stroke="#fff" stroke-width="0.8"/><path d="M0.7 5 H9.3 M1.5 2.8 H8.5 M1.5 7.2 H8.5" stroke="#fff" stroke-width="0.7"/></svg>
        <span class="web">www.lumarrastudio-example.com</span>
      </li>
    </ul>
    <p class="address">6128 N.Corbel Ridge Blvd Corvale Heights , CA 90377</p>
  </section>
</main>
</body>
</html>
```